Fabrication and machining company needing printed material designs.

Heron Vessels, Inc. wants to use appealing visuals as well as informative text to tell potential clients about our capabilities in fabrication and machining. We have a new logo to showcase as well as a new website. The use of print media will allow us to leave tangible information with clients, and therefore the design will need to be concise, informative, and visually appealing.

Full Page Flyer (approx. 8.5" x 11"), front and back design. This will be a detailed offering of capabilities and services for our shop.

Half Page Flyer (approx. 5.5" x 8.5"), front and back design. An abbreviated version of the full page flyer, meant to be easily handed out and stored inside a note book.

Bi-fold business card front and back. General offerings of our services. Minimal if any details. Finished size is twice the size of a business card (approx. 4" x 3.5"), once folded in half will be the same size as a standard business card (approx. 2" x 3.5").

Please use www.heronvesselsinc.example for theme ideas. The font used for our logo is ethnocentric, not to be used for all text.

Target Market(s)

Industrial Consumers

Font styles to use
Sans Serif

```html
<!DOCTYPE html>
<html lang="en">
<head>
<meta charset="utf-8">
<title>Heron Vessels, Inc. — Flyer</title>
<link href="https://fonts.googleapis.com/css2?family=Montserrat:ital,wght@0,300;0,400;0,700;0,800;1,300&display=swap" rel="stylesheet">
<style>
  :root {
    --orange: #fb4a06;
    --ink: #111111;
    --white: #ffffff;
    --steel-dark: #5f6466;
    --steel-mid: #a9adae;
    --steel-light: #e4e6e6;
    --text-dark: #1a1a1a;
  }
  html, body { margin: 0; padding: 0; overflow: hidden; }
  body { width: 849px; height: 1200px; background: var(--white); font-family: "Montserrat", sans-serif; }
  .flyer { position: relative; width: 849px; height: 1200px; overflow: hidden; background: var(--white); }
  .backdrop { position: absolute; inset: 0; }
  .brand { position: absolute; left: 51px; top: 112px; display: flex; align-items: center; gap: 10px; }
  .brand-square { width: 22px; height: 22px; background: var(--orange); }
  .brand-name { font-weight: 800; font-size: 19px; letter-spacing: 0.5px; color: var(--orange); text-transform: uppercase; white-space: nowrap; }
  .intro { position: absolute; left: 51px; top: 392px; width: 430px; margin: 0; font-weight: 400; font-size: 18px; line-height: 23px; color: var(--text-dark); white-space: nowrap; }
  .build-title { position: absolute; left: 49px; top: 510px; margin: 0; font-weight: 800; font-size: 53px; line-height: 60px; letter-spacing: -1px; color: var(--orange); white-space: nowrap; }
  .build-list { position: absolute; left: 51px; top: 566px; margin: 0; padding: 0; list-style: none; font-weight: 400; font-size: 24px; line-height: 31.4px; color: var(--text-dark); white-space: nowrap; }
  .facility { position: absolute; left: 390px; top: 711px; margin: 0; font-weight: 300; font-style: italic; font-size: 23px; line-height: 29px; color: var(--white); white-space: nowrap; }
  .facility sup { font-size: 12px; }
  .specialty { position: absolute; left: 390px; top: 781px; margin: 0; font-weight: 400; font-size: 25px; line-height: 31px; color: var(--white); white-space: nowrap; }
  .specialty strong { font-weight: 800; font-size: 27px; }
  .industries { position: absolute; left: 390px; top: 886px; }
  .industries-title { margin: 0; font-weight: 800; font-size: 26px; line-height: 32px; color: var(--orange); white-space: nowrap; }
  .industries-list { margin: 0; padding: 0; list-style: none; font-weight: 400; font-size: 23px; line-height: 28.7px; color: var(--white); white-space: nowrap; }
  .industries-list li { display: flex; }
  .industries-list li::before { content: "»"; width: 35px; font-size: 18px; }
  .call { position: absolute; left: 51px; top: 1088px; margin: 0; font-weight: 800; color: var(--white); white-space: nowrap; }
  .call-label { display: block; font-size: 24px; line-height: 31px; }
  .call-number { display: block; font-size: 26px; line-height: 33px; }
  .website { position: absolute; right: 52px; top: 1126px; margin: 0; font-weight: 800; font-size: 22px; color: var(--white); white-space: nowrap; }
</style>
</head>
<body>
<main class="flyer">
  <svg class="backdrop" width="849" height="1200" viewBox="0 0 849 1200">
    <defs>
      <linearGradient id="steel" x1="1" y1="0" x2="0" y2="1">
        <stop offset="0" stop-color="#5f6466"/>
        <stop offset="0.35" stop-color="#a9adae"/>
        <stop offset="0.75" stop-color="#e4e6e6"/>
        <stop offset="1" stop-color="#ffffff"/>
      </linearGradient>
    </defs>
    <polygon class="tank-photo" role="img" aria-label="Photo of tall steel storage tanks with a stair walkway" points="491,0 849,0 849,376 0,996 0,340" fill="url(#steel)"/>
    <polygon class="band-upper" points="0,342 258,163 258,240 0,418" fill="var(--orange)"/>
    <polygon class="band-lower" points="447,575 849,282 849,376 447,667" fill="var(--orange)"/>
    <polygon class="dark-field" points="0,996 447,667 849,376 849,1200 0,1200" fill="var(--ink)"/>
  </svg>

  <div class="brand">
    <span class="brand-square"></span>
    <span class="brand-name">Heron Vessels, Inc.</span>
  </div>

  <p class="intro">It is said great ideas start with a brilliant flash.<br>Likewise, we think a brilliant solution<br>starts with an arc. From concept to<br>construction we deliver results<br>for the long haul.</p>

  <h1 class="build-title">WE BUILD</h1>
  <ul class="build-list">
    <li>TANKS</li>
    <li>PIPING</li>
    <li>FIRETUBES</li>
    <li>WALKWAYS &amp; STAIRS</li>
    <li>PUMP SKIDS</li>
    <li>TRAILER COMPONENTS</li>
    <li>TANK VENTS</li>
    <li>CLARIFIERS</li>
  </ul>

  <p class="facility">A facility of 35,000 ft<sup>2</sup><br>and a 5 Acre storage yard</p>

  <p class="specialty">We specialize in<br><strong>API-12F &amp; API-650</strong><br>tank manufacturing</p>

  <section class="industries">
    <h2 class="industries-title">INDUSTRIES SERVED</h2>
    <ul class="industries-list">
      <li>Oil &amp; Gas</li>
      <li>Water &amp; Waste water</li>
      <li>Mining</li>
      <li>Aggregate</li>
      <li>Power Generation</li>
    </ul>
  </section>

  <p class="call"><span class="call-label">CALL US NOW</span><span class="call-number">(555) 014 - 7302</span></p>

  <p class="website">www.heronvesselsinc.example</p>
</main>
</body>
</html>
```